Infografik für unabhängigen Finanzdienstleister
Zielgruppe
Wir sind eine unabhängiger Finanzdienstleister mit dem Schwerpunkt der Kapitalanlage und dem Fokus auf vermögende Privatkunden. Wir sind nur unseren Mandanten verpflichtet, da diese unsere Dienstleistung transparent und frei von versteckten Provisionen honorieren.
Aufgabenstellung
Klassisch modern, aber nicht verspielt. Ein Gefühl gibt unsere Homepage. Weitere Infos zum Projekt habe ich hier in einem kurzen Video verfasst: https://lobark.vemiko-kanzlei.example/message?id=7f91c3a5e2d04b
Ergänzung:
Die Grafik soll sich mehr 'selbst erklären lassen' als sie es derzeit tut. Zudem soll die Prozessreihenfolge besser verdeutlicht werden...

```html
<!DOCTYPE html>
<html lang="de">
<head>
<meta charset="utf-8">
<title>Infografik – Beratungsprozess</title>
<link rel="stylesheet" href="https://fonts.googleapis.com/css2?family=Lexend:wght@400;600;700&display=swap">
<style>
  :root {
    --bg-light: #d9c38f;
    --bg-mid: #bf9c4c;
    --bg-dark: #a97b27;
    --cream: #eee0c4;
    --white: #ffffff;
    --gold: #b28a2c;
    --ink: #2b2620;
    --shadow: rgba(60, 40, 5, 0.35);
  }
  * { margin: 0; padding: 0; box-sizing: border-box; }
  html, body { width: 1200px; height: 574px; overflow: hidden; }
  body {
    font-family: "Lexend", sans-serif;
    color: var(--ink);
    background: linear-gradient(90deg, var(--bg-light) 0%, var(--bg-mid) 28%, #b28a30 55%, var(--bg-dark) 100%);
    position: relative;
  }
  .hex-layer { position: absolute; left: 0; top: 0; }
  .hex-label {
    position: absolute;
    font-size: 15.5px;
    line-height: 19.5px;
    font-weight: 400;
  }
  .portrait {
    position: absolute;
    left: 68px; top: 246px; width: 104px; height: 83px;
    border-radius: 40px 40px 6px 6px;
    background: linear-gradient(90deg, #e9a877 0%, #d9a05a 50%, #c29a2e 100%);
  }
  .step {
    position: absolute;
    left: 424px; width: 699px; height: 101px;
    background: var(--cream);
  }
  .step-arrow { position: absolute; left: -26px; top: 25px; }
  .step-label {
    position: absolute;
    left: 29px; top: 13px; width: 165px; height: 72px;
    background: var(--white);
    box-shadow: 4px 5px 8px var(--shadow);
    display: flex; align-items: center;
    color: var(--gold); font-weight: 700;
  }
  .step-number {
    flex: 0 0 49px;
    padding-left: 13px;
    font-size: 19px;
    letter-spacing: -0.5px;
    white-space: nowrap;
  }
  .step-title {
    flex: 1 1 auto;
    font-size: 15px;
    line-height: 17.5px;
    letter-spacing: -0.2px;
    white-space: nowrap;
  }
  .step-item {
    position: absolute;
    top: 0; height: 101px;
    display: flex; align-items: center;
    font-size: 15.5px; line-height: 19.5px;
    white-space: nowrap;
  }
</style>
</head>
<body>
  <svg class="hex-layer" width="420" height="574" viewBox="0 0 420 574" aria-hidden="true">
    <defs>
      <filter id="hexShadow" x="-20%" y="-20%" width="150%" height="150%">
        <feDropShadow dx="5" dy="6" stdDeviation="6" flood-color="#4a3206" flood-opacity="0.35"/>
      </filter>
    </defs>
    <g filter="url(#hexShadow)">
      <polygon points="206,60 285.5,103 285.5,189 206,232 126.5,189 126.5,103" fill="#eddfc3"/>
      <polygon points="293,200 372.5,243 372.5,328 293,371 213.5,328 213.5,243" fill="#eddfc3"/>
      <polygon points="207,340 286.5,383 286.5,469 207,512 127.5,469 127.5,383" fill="#eddfc3"/>
      <polygon points="122,200 203.5,243 203.5,330 122,374 40.5,330 40.5,243" fill="#ffffff"/>
    </g>
  </svg>

  <div class="portrait" role="img" aria-label="Illustration eines Paares: Frau und Mann als Mandanten"></div>

  <div class="hex-label" style="left:163px; top:108px;">Finanzieller<br>Erfolg/gute<br>Investment<br>Erfahrung</div>
  <div class="hex-label" style="left:253px; top:257px;">Weniger<br>Verwaltung,<br>mehr Zeit</div>
  <div class="hex-label" style="left:162px; top:391px;">Umfassender<br>Schutz von<br>Vermögen<br>und Familie</div>

  <section class="step" style="top:89px;">
    <svg class="step-arrow" width="44" height="51" viewBox="0 0 44 51" aria-hidden="true"><polygon points="0,0 44,25.5 0,51" fill="#eddfc3"/></svg>
    <div class="step-label"><span class="step-number">III.</span><span class="step-title">Aktive Beglei-<br>tung und<br>Optimierung</span></div>
    <div class="step-item" style="left:228px;">Zentraler Ansprech-<br>partner zum Thema<br>Finanzen</div>
    <div class="step-item" style="left:410px;">Notfallplan</div>
    <div class="step-item" style="left:549px;">Experten-<br>Netzwerk</div>
  </section>

  <section class="step" style="top:233px;">
    <svg class="step-arrow" width="44" height="51" viewBox="0 0 44 51" aria-hidden="true"><polygon points="0,0 44,25.5 0,51" fill="#eddfc3"/></svg>
    <div class="step-label"><span class="step-number">II.</span><span class="step-title">Nachhaltige<br>Umsetzung</span></div>
    <div class="step-item" style="left:228px;">Nobelpreisgekrönte<br>und erfolgreiche<br>Anlagestrategie</div>
    <div class="step-item" style="left:396px;">Berücksichtigung<br>steuerlicher<br>Aspekte</div>
    <div class="step-item" style="left:549px;">Transparente und<br>provisionsfreie<br>Vergütung</div>
  </section>

  <section class="step" style="top:371px;">
    <svg class="step-arrow" width="44" height="51" viewBox="0 0 44 51" aria-hidden="true"><polygon points="0,0 44,25.5 0,51" fill="#eddfc3"/></svg>
    <div class="step-label"><span class="step-number">I.</span><span class="step-title">Starkes<br>Fundament</span></div>
    <div class="step-item" style="left:228px;">Entwicklung eines<br>persönlichen<br>Finanzplanes</div>
    <div class="step-item" style="left:399px;">Wissens-<br>vermittlung</div>
    <div class="step-item" style="left:549px;">Tiefe Analyse Ihrer<br>IST-Situation und<br>Ihrer Ziele</div>
  </section>
</body>
</html>
```